New modern business card design

To design a brand new business card that's clean & modern in terms of layout.
I have attached our company logo and also basic information regarding what is needed on the card that also needs to be editable.

Target Market(s)

motor trade

Contact Information for Business Card

logo, name, title, tel, mob, email, address, www, all information is in the word.doc file

Requirements
Must have
• white background
Nice to have
• Nice clean font

```html
<!DOCTYPE html>
<html lang="en">
<head>
<meta charset="utf-8">
<title>Norbury Motors Ltd – Business Card</title>
<link rel="stylesheet" href="https://fonts.googleapis.com/css2?family=Arimo:wght@400;700&display=swap">
<style>
  :root {
    --page-bg: #2b2b2b;
    --card-white: #ffffff;
    --card-shade: #eef0f2;
    --brand-blue: #1e6aaa;
    --brand-blue-deep: #175a93;
    --swoosh-grey: #9ea1a5;
    --text-light: #ffffff;
    --text-soft: #dbe7f3;
  }
  * { box-sizing: border-box; margin: 0; padding: 0; }
  html, body {
    width: 1200px; height: 997px; overflow: hidden;
    background: var(--page-bg);
    font-family: "Arimo", Arial, sans-serif;
  }
  .business-card {
    position: absolute; left: 150px; top: 241px;
    width: 900px; height: 514px;
    background: linear-gradient(160deg, var(--card-white) 40%, var(--card-shade));
    overflow: hidden;
    box-shadow: 0 20px 40px rgba(0,0,0,.45);
  }
  .card-shapes { position: absolute; inset: 0; }
  .brand {
    position: absolute; left: 0; right: 0; top: 118px;
    text-align: center;
  }
  .brand-lockup {
    display: inline-flex; align-items: center; gap: 14px;
    padding-bottom: 14px;
    border-bottom: 2px solid var(--brand-blue);
  }
  .brand-mark {
    width: 30px; height: 30px; background: var(--brand-blue);
  }
  .brand-name {
    font-size: 42px; font-weight: 700; letter-spacing: 1px;
    color: var(--brand-blue);
  }
  .person {
    position: absolute; left: 120px; top: 370px; color: var(--text-light);
  }
  .person-name { font-size: 24px; font-weight: 700; letter-spacing: .5px; }
  .person-title { font-size: 19px; color: var(--text-soft); margin-top: 6px; padding-left: 56px; }
  .website {
    position: absolute; left: 120px; top: 460px;
    font-size: 18px; font-weight: 700; color: var(--text-light);
  }
  .divider {
    position: absolute; left: 462px; top: 282px; width: 1px; height: 150px;
    background: rgba(255,255,255,.55);
  }
  .contact-list {
    position: absolute; left: 482px; top: 280px; list-style: none;
    color: var(--text-light); font-size: 19px;
  }
  .contact-item { display: flex; align-items: flex-start; gap: 14px; margin-bottom: 10px; }
  .contact-icon { width: 22px; height: 22px; flex: none; margin-top: 1px; }
  .contact-text { line-height: 23px; }
</style>
</head>
<body>
  <article class="business-card">
    <svg class="card-shapes" width="900" height="514" viewBox="0 0 900 514" aria-hidden="true">
      <path d="M0,355 Q420,170 900,200 L900,514 L0,514 Z" fill="var(--brand-blue)"/>
      <path d="M0,430 L0,514 L900,514 L900,470 Q450,520 0,430 Z" fill="var(--brand-blue-deep)" opacity=".35"/>
      <path d="M40,345 Q420,150 880,180 Q430,165 40,345 Z" fill="var(--swoosh-grey)"/>
    </svg>

    <header class="brand">
      <div class="brand-lockup">
        <span class="brand-mark"></span>
        <span class="brand-name">NORBURY MOTORS LTD</span>
      </div>
    </header>

    <section class="person">
      <h1 class="person-name">DANIEL HARPER</h1>
      <p class="person-title">General Manager</p>
    </section>
    <p class="website">www.norbury-motors.co.uk</p>

    <div class="divider"></div>

    <ul class="contact-list">
      <li class="contact-item">
        <svg class="contact-icon" viewBox="0 0 22 22" aria-hidden="true"><circle cx="11" cy="11" r="11" fill="#fff"/><path d="M6 8c0-1 1-2 2-2h1l1 3-1 1c1 2 2 3 4 4l1-1 3 1v1c0 1-1 2-2 2C10 17 5 12 6 8z" fill="var(--brand-blue)"/></svg>
        <span class="contact-text">0161 555 0142</span>
      </li>
      <li class="contact-item">
        <svg class="contact-icon" viewBox="0 0 22 22" aria-hidden="true"><circle cx="11" cy="11" r="11" fill="#fff"/><rect x="7.5" y="4.5" width="7" height="13" rx="1.5" fill="var(--brand-blue)"/><rect x="8.5" y="6" width="5" height="8" fill="#fff"/></svg>
        <span class="contact-text">07700 900 418</span>
      </li>
      <li class="contact-item">
        <svg class="contact-icon" viewBox="0 0 22 22" aria-hidden="true"><circle cx="11" cy="11" r="11" fill="#fff"/><rect x="5" y="7" width="12" height="8" fill="var(--brand-blue)"/><path d="M5 7l6 5 6-5" fill="none" stroke="#fff" stroke-width="1.2"/></svg>
        <span class="contact-text">dharper@norbury-motors.co.uk</span>
      </li>
      <li class="contact-item">
        <svg class="contact-icon" viewBox="0 0 22 22" aria-hidden="true"><circle cx="11" cy="11" r="11" fill="#fff"/><path d="M11 4a4.5 4.5 0 0 0-4.5 4.5C6.5 12 11 18 11 18s4.5-6 4.5-9.5A4.5 4.5 0 0 0 11 4z" fill="var(--brand-blue)"/><circle cx="11" cy="8.5" r="1.7" fill="#fff"/></svg>
        <span class="contact-text">Mill Lane Trade Park<br>Manchester M40 2XY</span>
      </li>
    </ul>
  </article>
</body>
</html>
```